Academy Values Classroom Poster

Marrowdene Community Academy has the core values of Aspiration, Positivity, Responsibility and Achievement at its heart. We have these words displayed in our entrance (in Bliss font) but would like them to permeate into the classroom spaces in a poster form. We want a clear message that shows what the values mean to students:

Aspiration - Think BIG (pantone 717)
Positivity - Smile :-) (pantone 376)
Responsibility - for yourself and others (pantone 569)
Achievement - Celebrate Success! (pantone 214)

It would be good to follow the colour scheme of the main words to create a 'brand' for these values (pantone refs noted in brackets) and we would like to see some clean designs please.

I anticipate these will be A1 posters.

I have attached our school logo although it is not essential that this is included.

Target Market(s)

Students

Industry/Entity Type

School

Font styles to use
Other font styles liked:
• Bliss or Segoe UI

Requirements
Must have
• Aspiration - Think BIG
Positivity - Smile :-)
Responsibility - for yourself and others
Achievement - Celebrate Success!
Should not have
• Nothing too busy

```html
<!DOCTYPE html>
<html lang="en">
<head>
<meta charset="utf-8">
<title>Academy Values Poster</title>
<link rel="stylesheet" href="https://fonts.googleapis.com/css2?family=Open+Sans:ital,wght@0,400;0,600;1,400&display=swap">
<style>
  :root {
    --aspiration: #d4622a;
    --positivity: #84bf41;
    --responsibility: #007f6e;
    --achievement: #d41c69;
    --white: #ffffff;
    --navy: #1f3552;
    --bg-light: #f4f7f9;
    --bg-deep: #78aec6;
  }
  * { margin: 0; padding: 0; box-sizing: border-box; }
  html, body { width: 1200px; height: 848px; overflow: hidden; }
  body {
    font-family: "Open Sans", "Segoe UI", sans-serif;
    background: linear-gradient(32deg, var(--bg-light) 0%, #c9dde7 45%, var(--bg-deep) 100%);
    position: relative;
  }
  .values-grid {
    position: absolute;
    left: 45px; top: 45px;
    width: 1113px; height: 710px;
    display: grid;
    grid-template-columns: 555px 558px;
    grid-template-rows: 356px 354px;
  }
  .value {
    position: relative;
    color: var(--white);
  }
  .value--aspiration { background: var(--aspiration); }
  .value--positivity { background: var(--positivity); }
  .value--responsibility { background: var(--responsibility); }
  .value--achievement { background: var(--achievement); }
  .value__name {
    position: absolute;
    left: 0; right: 0; top: 148px;
    text-align: center;
    font-weight: 400;
    font-size: 42px;
    letter-spacing: -0.5px;
    line-height: 1;
  }
  .value__star {
    font-size: 34px;
    vertical-align: 16px;
    margin-left: 2px;
  }
  .value__meaning {
    position: absolute;
    right: 18px; bottom: 12px;
    font-style: italic;
    font-size: 23px;
  }
  .value__meaning .value__star {
    font-size: 20px;
    vertical-align: 10px;
    margin: 0 4px 0 0;
    font-style: normal;
  }
  .academy-mark {
    position: absolute;
    right: 42px; top: 784px;
    display: flex;
    align-items: center;
    gap: 12px;
  }
  .academy-mark__square {
    width: 40px; height: 40px;
    background: var(--navy);
  }
  .academy-mark__name {
    color: var(--navy);
    font-weight: 600;
    font-size: 20px;
    line-height: 1.1;
  }
</style>
</head>
<body>
  <main class="values-grid">
    <section class="value value--aspiration">
      <h2 class="value__name">ASPIRATION<span class="value__star">*</span></h2>
      <p class="value__meaning"><span class="value__star">*</span>Think BIG</p>
    </section>
    <section class="value value--positivity">
      <h2 class="value__name">POSITIVITY<span class="value__star">*</span></h2>
      <p class="value__meaning"><span class="value__star">*</span>Smile</p>
    </section>
    <section class="value value--responsibility">
      <h2 class="value__name">RESPONSIBILITY<span class="value__star">*</span></h2>
      <p class="value__meaning"><span class="value__star">*</span>for yourself and others</p>
    </section>
    <section class="value value--achievement">
      <h2 class="value__name">ACHIEVEMENT<span class="value__star">*</span></h2>
      <p class="value__meaning"><span class="value__star">*</span>Celebrate Success!</p>
    </section>
  </main>
  <footer class="academy-mark">
    <span class="academy-mark__square"></span>
    <span class="academy-mark__name">Marrowdene<br>Community Academy</span>
  </footer>
</body>
</html>
```